Professional Learning Organization for Educators needs a Design Thinking Workshop Flyer

We need a flyer for a series of Introductory Design Thinking workshops we're delivering for education leaders.

We have generated our own version of the flyer with a word template, but want it to look even more professional and eye catching. It is attached.

We had an image that we thought might be good, but pulled it out so we don't bias designers' thinking.
Updates

Reason: We are a bit flexible on the deadline since this is a holiday week and people are traveling

Target Market(s)

Very busy education leaders whose curiosity needs to be stimulated enough to enroll in the course

Industry/Entity Type

Education

Font styles to use
Other font styles liked:
• Century Gothic or something closer to that

Requirements
Must have
• Some version of the text that is on the current flyer that I attached.
Nice to have
• I am very flexible and open right now on this design.

```html
<!DOCTYPE html>
<html lang="en">
<head>
<meta charset="utf-8">
<title>Design Thinking Workshops Flyer</title>
<link href="https://fonts.googleapis.com/css2?family=Mulish:wght@400;600;800;900&display=swap" rel="stylesheet">
<style>
  :root{
    --navy:#2a2f8c;
    --blue:#1274c0;
    --ink:#2f2f38;
    --panel:#d2eeec;
    --stage:#e4e4e4;
    --white:#ffffff;
  }
  *{box-sizing:border-box;margin:0;padding:0}
  html,body{width:1200px;height:1200px;overflow:hidden;background:var(--stage)}
  body{font-family:"Mulish",sans-serif;color:var(--ink);position:relative}
  .flyer{position:absolute;left:185px;top:15px;width:830px;height:1170px;background:var(--white);overflow:hidden;box-shadow:0 4px 18px rgba(0,0,0,.18)}
  .flyer-shapes{position:absolute;inset:0;width:830px;height:1170px}
  .abs{position:absolute}
  .title{left:26px;top:28px;font-weight:900;line-height:.98;letter-spacing:1px}
  .title span{display:block;-webkit-text-stroke:3px var(--white);paint-order:stroke fill}
  .title .t1{font-size:82px;color:var(--navy)}
  .title .t2{font-size:82px;color:var(--blue)}
  .title .t3{font-size:64px;color:var(--navy);margin-top:6px}
  .intro{left:60px;top:520px;width:370px}
  .intro h2{font-size:30px;font-weight:800;color:var(--navy);letter-spacing:1.5px;line-height:1}
  .intro .sub{font-size:22px;color:var(--blue);margin-top:4px}
  .intro p{font-size:14px;line-height:1.42;margin-top:12px;text-align:justify}
  .benefits{list-style:none;margin-top:14px;padding-left:16px}
  .benefits li{position:relative;font-size:14px;color:var(--navy);line-height:1.42;padding-left:22px;margin-bottom:10px}
  .benefits li::before{content:"";position:absolute;left:0;top:5px;width:12px;height:12px;background:var(--blue)}
  .offer{left:76px;top:905px;width:354px;font-size:13.5px;line-height:1.35}
  .offer b{font-size:20px;font-weight:800}
  .schedule{left:76px;top:975px;width:370px;font-size:14.5px;line-height:1.3}
  .schedule .day{color:var(--navy);font-size:16.5px}
  .schedule .row{display:flex;gap:24px;margin-bottom:4px}
  .schedule .line{margin-top:2px}
  .quotes{left:494px;top:560px;width:300px}
  .quotes h2{font-size:28px;font-weight:600;color:var(--navy);line-height:1}
  .quotes .sub{font-size:22px;color:var(--navy);margin-top:4px;letter-spacing:1px}
  .quotes blockquote{font-size:13.5px;line-height:1.5;margin-top:24px}
  .contact{left:520px;top:920px;width:300px}
  .contact .org{font-size:17px;font-weight:600;letter-spacing:.5px}
  .contact .url{font-size:25px;color:var(--navy);margin-top:2px}
  .contact .q{font-size:20px;margin-top:30px}
  .contact .mail{font-size:21px;color:var(--navy);margin-top:2px}
  .footer{left:30px;top:1104px;width:780px;font-size:14px;white-space:nowrap}
  .footer .cta{font-size:22px;color:var(--navy)}
  .footer .url{font-size:22px;color:var(--navy)}
  .footer .note{font-size:13.5px;margin-top:4px}
</style>
</head>
<body>
<div class="flyer">
  <svg class="flyer-shapes" viewBox="0 0 830 1170">
    <defs>
      <linearGradient id="photoTone" x1="0" y1="0" x2="1" y2="1">
        <stop offset="0" stop-color="#d9d3d6"/>
        <stop offset=".45" stop-color="#b7806a"/>
        <stop offset=".75" stop-color="#8fa6c6"/>
        <stop offset="1" stop-color="#c9b9a8"/>
      </linearGradient>
    </defs>
    <rect x="0" y="0" width="830" height="610" fill="url(#photoTone)" role="img" aria-label="Photo of smiling young educators giving a thumbs up in a library"/>
    <path d="M0,345 C140,450 360,470 452,600 L452,1170 L0,1170 Z" fill="var(--white)"/>
    <path d="M452,600 C510,470 670,350 830,235 L830,1170 L452,1170 Z" fill="var(--white)"/>
    <path d="M0,290 C160,380 380,400 452,600 C370,440 150,420 0,325 Z" fill="var(--navy)"/>
    <path d="M0,325 C150,420 370,440 452,600 C360,470 140,450 0,345 Z" fill="var(--blue)"/>
    <path d="M830,140 C640,260 470,400 452,600 C500,450 660,330 830,220 Z" fill="var(--navy)"/>
    <path d="M830,220 C660,330 500,450 452,600 C510,470 670,350 830,235 Z" fill="var(--blue)"/>
    <path d="M830,250 C675,355 520,470 470,610 C465,800 470,1000 480,1090 L830,1090 Z" fill="var(--panel)"/>
    <line x1="0" y1="1091" x2="830" y2="1091" stroke="var(--blue)" stroke-width="2"/>
  </svg>

  <h1 class="abs title">
    <span class="t1">DESIGN</span>
    <span class="t2">THINKING</span>
    <span class="t3">WORKSHOPS</span>
  </h1>

  <section class="abs intro">
    <h2>DESIGNING</h2>
    <div class="sub">your way to better solutions.</div>
    <p>Maple Ridge Public Schools and Highline Learning Co-op invite you to discover the power of Design Thinking. During our three session course, you will learn and practice mindsets and tools that help you continuously and creatively improve the experiences of the people you serve by:</p>
    <ul class="benefits">
      <li>Understanding what your teachers, students and community truly need in their learning and work experiences</li>
      <li>Designing solutions that better meet their needs</li>
      <li>Seeking authentic feedback and reactions to these solutions prior to their implementation.</li>
    </ul>
  </section>

  <p class="abs offer"><b>We</b> are offering this three-session course at four different times in spring semester. Please choose the course that works best for your schedule.</p>

  <div class="abs schedule">
    <div class="row">
      <div><div class="day">Monday mornings:</div>1/23, 1/30 and 2/6</div>
      <div><div class="day">Tuesday afternoons:</div>2/7, 2/14 and 2/21</div>
    </div>
    <div class="line"><span class="day">Wednesday afternoons:</span> 3/8, 3/15 and 3/22</div>
    <div class="line"><span class="day">Wednesday evenings:</span> 2/8, 2/15 and 2/22</div>
  </div>

  <section class="abs quotes">
    <h2>What our</h2>
    <div class="sub">participants say...</div>
    <blockquote>“This has been an empowering experience that allowed me to try out dramatic changes in my practice that I wouldn’t have imagined before.”</blockquote>
    <blockquote>“I never realized how often I’ve guessed and assumed what our teachers and students need now I have a way to stop guessing!”</blockquote>
    <blockquote>“I finally have tools to generate truly creative ideas that people actually embrace... because they meet their needs”</blockquote>
  </section>

  <div class="abs contact">
    <div class="org">HIGHLINE LEARNING CO-OP</div>
    <div class="url">www.highlinecoop.org</div>
    <div class="q">Questions?</div>
    <div class="mail">H.Garner@ridgeschools.org</div>
  </div>

  <footer class="abs footer">
    <div><span class="cta">Click here</span> to enroll. Go to <span class="url">www.highlinecoop.org</span> to learn more.</div>
    <div class="note">This course is held in Maple Ridge Public Schools. No fee for MRPS leaders. $150 fee for leaders outside of MRPS.</div>
  </footer>
</div>
</body>
</html>
```